Creation of a cover for a book on popular ideas (received relief, preconceived ideas).
The picture (either photos or drawings) should represent a or several sheeps in a (French) city. The reason for this is that in France, people following general opinions are pictured as sheeps (following the herd )
Size: 11 x 17.8 cm
AUTHOR: Lucien-Mathis Vorrel
TITLE: Handbook of quiet garden walks
PUBLISHER: Korvane Editions (at the bottom of the page)

General adult public

Book

```html
<!DOCTYPE html>
<html lang="en">
<head>
<meta charset="utf-8">
<title>Handbook of quiet garden walks — Book Cover</title>
<link rel="stylesheet" href="https://fonts.googleapis.com/css2?family=Anton&family=Caveat:wght@500&family=Source+Serif+4:opsz,wght@8..60,600;8..60,700&display=swap">
<style>
  :root {
    --page-bg: #dcdcdc;
    --sky-top: #00c8ee;
    --sky-mid: #4fc3e2;
    --haze: #a9cbd6;
    --city-light: #c7c3b8;
    --city-mid: #8c98a0;
    --ground: #2b5a6c;
    --ground-deep: #0d2f3e;
    --wool-light: #ddd6c1;
    --wool-mid: #c5bca2;
    --wool-shade: #a39a82;
    --ink: #10212b;
    --accent-red: #d11a1a;
    --bubble: #ffffff;
    --title-fill: #ffffff;
    --title-ice: #c4ecf6;
  }
  * { margin: 0; padding: 0; box-sizing: border-box; }
  html, body {
    width: 1200px; height: 960px; overflow: hidden;
    background: var(--page-bg);
  }
  .cover {
    position: absolute; left: 328px; top: 40px;
    width: 544px; height: 880px; overflow: hidden;
    background: linear-gradient(180deg, var(--sky-top) 0%, var(--sky-mid) 24%, var(--haze) 40%);
  }
  .cityscape-photo {
    position: absolute; left: 0; top: 330px; width: 100%; height: 550px;
    background: linear-gradient(180deg,
      rgba(169,203,214,0) 0%,
      var(--city-light) 12%,
      var(--city-mid) 34%,
      var(--ground) 62%,
      var(--ground-deep) 100%);
  }
  .sheep-photo {
    position: absolute; left: 140px; top: 370px; width: 470px; height: 560px;
    border-radius: 46% 40% 0 0 / 38% 34% 0 0;
    background: radial-gradient(ellipse 60% 55% at 42% 40%, var(--wool-light) 0%, var(--wool-mid) 60%, var(--wool-shade) 100%);
  }
  .author {
    position: absolute; top: 78px; left: 0; width: 100%;
    text-align: center;
    font-family: "Source Serif 4", serif; font-weight: 700;
    font-size: 29px; color: var(--ink);
  }
  .bubbles { position: absolute; inset: 0; }
  .title {
    position: absolute; top: 156px; left: 0; width: 100%;
    text-align: center;
    font-family: "Anton", sans-serif; font-weight: 400;
    font-size: 112px; line-height: 1.05;
    letter-spacing: 0;
    background: linear-gradient(180deg, var(--title-fill) 0%, var(--title-fill) 52%, var(--title-ice) 56%, var(--title-ice) 100%);
    -webkit-background-clip: text; background-clip: text; color: transparent;
    -webkit-text-stroke: 1.5px var(--accent-red);
    filter: drop-shadow(2px 3px 0 var(--ink));
  }
  .subtitle {
    position: absolute; top: 276px; left: 73px; width: 400px;
    text-align: center;
    font-family: "Source Serif 4", serif; font-weight: 600;
    font-size: 29px; color: var(--ink);
  }
  .circled { position: relative; }
  .circled::after {
    content: ""; position: absolute;
    left: -8px; right: -6px; top: 4px; bottom: -6px;
    border: 2px solid var(--accent-red); border-radius: 50%;
    transform: rotate(-9deg);
  }
  .bubble-word {
    position: absolute;
    font-family: "Caveat", cursive; font-weight: 500; color: var(--accent-red);
  }
  .bubble-word.right { left: 404px; top: 360px; font-size: 34px; transform: rotate(6deg); }
  .bubble-word.left { left: 72px; top: 502px; font-size: 27px; transform: rotate(-4deg); }
  .publisher {
    position: absolute; left: 49px; top: 805px;
    width: 159px; height: 32px;
    background: var(--accent-red);
    display: flex; align-items: center; justify-content: center;
    font-family: "Source Serif 4", serif; font-weight: 600;
    font-size: 17px; color: #ffffff;
  }
</style>
</head>
<body>
  <div class="cover">
    <div class="cityscape-photo" role="img" aria-label="Photograph of a hazy Paris cityscape seen from above, with the Eiffel Tower rising behind the title, fading to dark blue at the bottom"></div>
    <div class="sheep-photo" role="img" aria-label="Photograph of a large woolly white sheep with curly fleece, head turned toward the viewer, filling the lower right of the cover"></div>

    <p class="author">Lucien-Mathis Vorrel</p>

    <svg class="bubbles" width="544" height="880" viewBox="0 0 544 880" aria-hidden="true">
      <path d="M272 238 C160 238 73 262 73 298 C73 332 128 354 196 360 L225 388 L214 360 C240 362 260 362 272 362 C383 362 472 336 472 298 C472 262 383 238 272 238 Z" fill="var(--bubble)"/>
      <path d="M434 352 C392 352 358 366 358 386 C358 404 384 416 418 418 L436 432 L440 418 C480 416 509 403 509 386 C509 366 476 352 434 352 Z" fill="var(--bubble)"/>
      <path d="M93 494 C62 494 38 507 38 523 C38 536 52 546 72 550 L92 566 L86 552 C122 552 148 540 148 523 C148 507 124 494 93 494 Z" fill="var(--bubble)"/>
    </svg>

    <h1 class="title">HANDBOOK</h1>
    <p class="subtitle">of <span class="circled">quiet</span> garden walks</p>

    <span class="bubble-word right">idea</span>
    <span class="bubble-word left">idea</span>

    <div class="publisher">Korvane Editions</div>
  </div>
</body>
</html>
```